High Tech Real Estate Startup needs a business card

We are developing an innovative real estate marketing product based around advanced search and virtual reality.

We talk to people, we need business cards.

Target Market(s)

The target market is technology professionals and realtors.

Contact Information for Business Card

The information to be included will include

Name
Title
Phone Number
E-mail Address
www.quelzo.com

It should use simple iconography for each one of those fields.

Font styles to use
Other font styles liked:
• Co, Jubilat, Avenir

Colors

Designer to choose colors to be used in the design.

Requirements
Must have
• Clean aesthetic,
• Good use of negative space.
• It should use our company logo, shown in the attached file. It is able to use the negative of that logo (coloured font and white background) and I have attached other acceptable accent colours in a swatch file.
Should not have
• Should not be too busy
• No extraneous text (slogans, tag lines etc)

```html
<!DOCTYPE html>
<html lang="en">
<head>
<meta charset="utf-8">
<title>Quelzo Business Card</title>
<link href="https://fonts.googleapis.com/css2?family=Mulish:wght@400;700;800&display=swap" rel="stylesheet">
<style>
  :root {
    --coral: #F27C57;
    --coral-soft: #F6A487;
    --sun: #F5B451;
    --crimson: #B3163F;
    --paper: #FFFFFF;
  }
  * { margin: 0; padding: 0; box-sizing: border-box; }
  html, body {
    width: 1200px;
    height: 1000px;
    overflow: hidden;
    background: var(--paper);
    font-family: "Mulish", "Avenir", sans-serif;
  }
  .canvas { position: relative; width: 1200px; height: 1000px; }

  .card-front {
    position: absolute;
    left: 39px; top: 230px;
    width: 828px; height: 265px;
    background: var(--coral);
  }
  .brand-name {
    position: absolute;
    left: 183px; top: 178px;
    font-weight: 400;
    font-size: 128px;
    line-height: 1;
    letter-spacing: 4px;
    color: var(--sun);
  }

  .card-back {
    position: absolute;
    left: 39px; top: 502px;
    width: 828px; height: 485px;
    background: var(--paper);
    overflow: hidden;
  }
  .brush-texture {
    position: absolute;
    right: 0; top: 0;
    width: 300px; height: 485px;
  }

  .identity {
    position: absolute;
    right: 273px; top: 200px;
    text-align: right;
  }
  .person-name {
    font-weight: 800;
    font-size: 35px;
    line-height: 1;
    letter-spacing: -0.5px;
    color: var(--crimson);
  }
  .person-title {
    margin-top: 3px;
    font-weight: 400;
    font-size: 17px;
    letter-spacing: 2px;
    color: var(--coral);
  }

  .contact-list {
    position: absolute;
    left: 139px; top: 292px;
    list-style: none;
  }
  .contact-item {
    display: flex;
    align-items: center;
    height: 40px;
    margin-bottom: 1px;
  }
  .contact-icon {
    width: 26px; height: 26px;
    margin-right: 15px;
    fill: var(--crimson);
    color: var(--crimson);
  }
  .contact-text {
    font-size: 18px;
    letter-spacing: 2.4px;
    color: var(--coral);
  }
</style>
</head>
<body>
<main class="canvas">
  <section class="card-front">
  </section>
  <h1 class="brand-name">QUELZO</h1>

  <section class="card-back">
    <svg class="brush-texture" viewBox="0 0 300 485" role="img" aria-label="Coral paint brush strokes texture">
      <defs>
        <linearGradient id="brushFade" x1="0" y1="0" x2="1" y2="0">
          <stop offset="0" stop-color="#F27C57" stop-opacity="0.35"/>
          <stop offset="0.5" stop-color="#F27C57" stop-opacity="0.9"/>
          <stop offset="1" stop-color="#F27C57"/>
        </linearGradient>
      </defs>
      <polygon points="40,0 300,0 300,485 110,485 60,300 0,60" fill="url(#brushFade)"/>
    </svg>

    <div class="identity">
      <p class="person-name">JOHN SMITH</p>
      <p class="person-title">EXECUTIVE ASSISTANT</p>
    </div>

    <ul class="contact-list">
      <li class="contact-item">
        <svg class="contact-icon" viewBox="0 0 24 24" aria-hidden="true">
          <path d="M6.6 10.8c1.4 2.8 3.8 5.1 6.6 6.6l2.2-2.2c.3-.3.7-.4 1-.2 1.1.4 2.3.6 3.6.6.6 0 1 .4 1 1V20c0 .6-.4 1-1 1C10.6 21 3 13.4 3 4c0-.6.4-1 1-1h3.5c.6 0 1 .4 1 1 0 1.3.2 2.5.6 3.6.1.3 0 .7-.2 1L6.6 10.8z"/>
        </svg>
        <span class="contact-text">000-000-0000</span>
      </li>
      <li class="contact-item">
        <svg class="contact-icon" viewBox="0 0 24 24" aria-hidden="true">
          <text x="12" y="19" text-anchor="middle" font-family="Mulish, sans-serif" font-weight="700" font-size="22" fill="currentColor">@</text>
        </svg>
        <span class="contact-text">JOHNSMITH@QUELZO.COM</span>
      </li>
      <li class="contact-item">
        <svg class="contact-icon" viewBox="0 0 24 24" aria-hidden="true" fill="none" stroke="currentColor" stroke-width="2.4" stroke-linecap="round">
          <path d="M10 14a4 4 0 0 0 5.7 0l3.5-3.5a4 4 0 0 0-5.7-5.7l-1.4 1.4"/>
          <path d="M14 10a4 4 0 0 0-5.7 0l-3.5 3.5a4 4 0 0 0 5.7 5.7l1.4-1.4"/>
        </svg>
        <span class="contact-text">WWW.QUELZO.COM</span>
      </li>
    </ul>
  </section>
</main>
</body>
</html>
```